I am looking for help designing my new business cards. I would like rounded edges and a raised logo on the back of the card. I have 2 Logos. One with a boat in it and one without. I'd like the one on the back to be the one that includes the boat and just the name on the front. I have included multiple formats of my logo. Please let me know if you need anymore.

Target Market(s)

Potential buyers and other sales brokers

Industry/Entity Type

Sales - Yacht / Boat Sales

Contact Information for Business Card

Id liike the front to include just the business name portion of the logo along with my name (Corwin Dalby), phone number (555.318.6027), website address (www.dalbymarineco.example) and not my physical address but just "Port Wrenley, SC". The back should include my full logo that has the boat included. This portion I'd prefer raised amd take up the majority of the space there. Thanks!!

Colors
0054AA
0677BA
7BADD7
CADEEF
E8F1F8
0094D4
00A9DD
6FCCEA
C7EBF8
E9F6FB

Requirements
Must have
• Double sided
Nice to have
• My email address: Corwin@dalbymarineco.example The NMTG logo somewhere small on the front of the card
Should not have
• My full address, prefer only "Port Wrenley, SC"

```html
<!DOCTYPE html>
<html lang="en">
<head>
<meta charset="utf-8">
<title>Dalby Marine Co. — Business Card</title>
<link rel="stylesheet" href="https://fonts.googleapis.com/css2?family=Lato:wght@400;700;900&display=swap">
<style>
  :root {
    --navy: #0a2a66;
    --navy-deep: #06245e;
    --brand-blue: #0054aa;
    --sea-blue: #0677ba;
    --sky-blue: #0094d4;
    --light-blue: #7badd7;
    --ink: #0a2a66;
    --text-grey: #5b5f66;
    --paper: #ffffff;
    --backdrop: #2b2e33;
  }
  * { box-sizing: border-box; margin: 0; padding: 0; }
  html, body {
    width: 1200px; height: 952px; overflow: hidden;
    background: var(--backdrop);
    font-family: "Lato", sans-serif;
  }
  .stage { position: relative; width: 1200px; height: 952px; }
  .card {
    position: absolute; top: 333px;
    width: 520px; height: 297px;
    border-radius: 26px;
    overflow: hidden;
    box-shadow: 0 14px 30px rgba(0,0,0,0.45);
  }
  .card-front { left: 50px; background: var(--paper); }
  .card-back { left: 630px; background: var(--navy-deep); }

  .hull-art { position: absolute; left: 0; top: 0; width: 100%; height: 100%; }

  .wordmark {
    position: absolute;
    font-weight: 900;
    text-transform: uppercase;
    line-height: 1;
    letter-spacing: 1px;
    white-space: nowrap;
  }
  .card-front .wordmark {
    left: 28px; top: 26px;
    font-size: 30px; color: var(--brand-blue);
  }
  .card-back .wordmark {
    left: 0; right: 0; top: 128px;
    text-align: center;
    font-size: 40px; color: var(--paper);
  }

  .holder { position: absolute; right: 30px; top: 120px; text-align: right; }
  .holder-name {
    font-weight: 900; font-size: 21px; color: var(--ink);
    text-transform: uppercase; letter-spacing: 0.5px;
  }
  .holder-role {
    font-size: 13px; color: var(--text-grey); margin-top: 2px;
    padding-bottom: 5px;
    border-bottom: 2px solid var(--sky-blue);
    display: inline-block;
  }

  .contact-list { position: absolute; right: 30px; top: 188px; list-style: none; text-align: right; }
  .contact-list li {
    display: flex; align-items: center; justify-content: flex-end;
    gap: 8px; height: 21px;
    font-size: 13px; color: var(--text-grey);
    white-space: nowrap;
  }
  .contact-icon {
    width: 17px; height: 17px; border-radius: 4px;
    background: var(--sky-blue);
    display: inline-flex; align-items: center; justify-content: center;
    flex: none;
  }
  .contact-icon svg { width: 11px; height: 11px; }
</style>
</head>
<body>
<main class="stage">

  <section class="card card-front" aria-label="Business card front">
    <svg class="hull-art" viewBox="0 0 520 297" role="img" aria-label="Illustration of a centre-console boat hull cutting through water">
      <path d="M0 175 C120 170 230 220 340 297 L0 297 Z" fill="var(--sea-blue)"/>
      <path d="M0 200 C110 198 200 240 270 297 L0 297 Z" fill="var(--brand-blue)" opacity="0.55"/>
    </svg>

    <div class="wordmark">Dalby Marine Co.</div>

    <div class="holder">
      <div class="holder-name">Corwin Dalby</div>
      <div class="holder-role">Managing Director</div>
    </div>

    <ul class="contact-list">
      <li>555.318.6027
        <span class="contact-icon"><svg viewBox="0 0 12 12"><path d="M3 1 L5 3.5 L4 5 C4.6 6.4 5.6 7.4 7 8 L8.5 7 L11 9 L9.8 11 C5.5 10.6 1.4 6.5 1 2.2 Z" fill="#fff"/></svg></span>
      </li>
      <li>Corwin@dalbymarineco.example
        <span class="contact-icon"><svg viewBox="0 0 12 12"><rect x="1" y="2.5" width="10" height="7" fill="none" stroke="#fff" stroke-width="1.2"/><path d="M1 2.5 L6 6.5 L11 2.5" fill="none" stroke="#fff" stroke-width="1.2"/></svg></span>
      </li>
      <li>www.dalbymarineco.example
        <span class="contact-icon"><svg viewBox="0 0 12 12"><path d="M6 1 L10 11 L6 8.5 L2 11 Z" fill="#fff"/></svg></span>
      </li>
      <li>Port Wrenley, SC
        <span class="contact-icon"><svg viewBox="0 0 12 12"><path d="M6 11 C3 7.5 2 6 2 4.5 A4 4 0 0 1 10 4.5 C10 6 9 7.5 6 11 Z" fill="#fff"/><circle cx="6" cy="4.5" r="1.4" fill="var(--sky-blue)"/></svg></span>
      </li>
    </ul>
  </section>

  <section class="card card-back" aria-label="Business card back">
    <div class="wordmark">Dalby Marine Co.</div>
  </section>

</main>
</body>
</html>
```